Income Tax Flyer - Updates Needed

Just need to update this flyer design and give it a new look. We would like to keep all the same wording but make it stand out a little more. Our selling point is the "Same Day Tax Advance up to $6,000"

Industry/Entity Type

Lending, Small Loans, Tax Services, Title Loans, Personal Loans

```html
<!DOCTYPE html>
<html lang="en">
<head>
<meta charset="utf-8">
<title>Tax Advance Flyer</title>
<link rel="stylesheet" href="https://fonts.googleapis.com/css2?family=Oswald:wght@600;700&family=Roboto:wght@400;500;700;900&display=swap">
<style>
  :root {
    --bg: #f1f1f1;
    --paper: #ffffff;
    --green: #2e7d4a;
    --green-dark: #285a3a;
    --green-text: #1f5a34;
    --red: #c3282e;
    --red-dark: #960d14;
    --white: #ffffff;
  }
  html, body {
    margin: 0;
    width: 1200px;
    height: 752px;
    overflow: hidden;
    background: var(--bg);
  }
  .stage {
    width: 1200px;
    height: 752px;
    display: flex;
    align-items: center;
    justify-content: center;
  }
  .flyer {
    width: 500px;
    height: 715px;
    background: var(--paper);
    box-shadow: 0 12px 30px rgba(0,0,0,0.18);
    display: block;
  }
  .display { font-family: "Oswald", "Arial Narrow", sans-serif; font-weight: 700; }
  .body-text { font-family: "Roboto", Arial, sans-serif; }
</style>
</head>
<body>
<main class="stage">
  <svg class="flyer" viewBox="0 0 720 1030" xmlns="http://www.w3.org/2000/svg">
    <defs>
      <linearGradient id="red-band" x1="0" y1="0" x2="0" y2="1">
        <stop offset="0" stop-color="#c9323a"/>
        <stop offset="1" stop-color="#9a0f16"/>
      </linearGradient>
      <linearGradient id="gold-type" x1="0" y1="0" x2="0" y2="1">
        <stop offset="0" stop-color="#fff6b8"/>
        <stop offset="0.5" stop-color="#f3d164"/>
        <stop offset="1" stop-color="#d9a52c"/>
      </linearGradient>
      <linearGradient id="photo-tone" x1="0" y1="0" x2="1" y2="1">
        <stop offset="0" stop-color="#eef0f3"/>
        <stop offset="0.55" stop-color="#d9d6d2"/>
        <stop offset="1" stop-color="#b9aea4"/>
      </linearGradient>
      <path id="apply-arc" d="M232 420 Q360 270 488 420"/>
    </defs>

    <!-- hero -->
    <polygon class="hero-band" points="0,312 720,165 720,400 0,400" fill="var(--green)"/>
    <rect class="hero-photo" x="40" y="130" width="630" height="270" fill="url(#photo-tone)"
          role="img" aria-label="Photo of two smiling business people giving a high five"/>

    <!-- brand -->
    <g class="brand">
      <circle cx="478" cy="80" r="8" fill="var(--green-dark)"/>
      <text class="body-text" x="690" y="88" font-size="22" font-weight="700" fill="var(--green-dark)" text-anchor="end">Keystone Lending</text>
    </g>

    <!-- offer band -->
    <path class="offer-band" d="M0 400 H205 Q360 210 515 400 H720 V563 H450 L360 597 L270 563 H0 Z" fill="url(#red-band)"/>
    <text class="display" font-size="50" fill="var(--white)" letter-spacing="2">
      <textPath href="#apply-arc" startOffset="50%" text-anchor="middle">APPLY HERE</textPath>
    </text>
    <text class="display" x="360" y="432" font-size="40" fill="var(--white)" text-anchor="middle">FOR</text>
    <text class="display" x="83" y="525" font-size="96" fill="url(#gold-type)" textLength="555" lengthAdjust="spacingAndGlyphs">$5,000 - $6000</text>

    <!-- headline -->
    <text class="body-text" x="360" y="640" font-size="36" font-weight="700" fill="var(--red)" text-anchor="middle">File your taxes and apply for an</text>
    <g class="rule" stroke="var(--green-dark)" stroke-width="2">
      <line x1="0" y1="695" x2="130" y2="695"/>
      <line x1="52" y1="687" x2="130" y2="687"/>
      <line x1="82" y1="703" x2="130" y2="703"/>
      <line x1="588" y1="695" x2="720" y2="695"/>
      <line x1="588" y1="687" x2="666" y2="687"/>
      <line x1="588" y1="703" x2="636" y2="703"/>
    </g>
    <text class="body-text" x="360" y="713" font-size="50" font-weight="900" fill="var(--green-dark)" text-anchor="middle">EASY ADVANCE!</text>

    <!-- features -->
    <g class="feature-icons" fill="none" stroke="var(--green-dark)" stroke-width="2.5">
      <circle cx="133" cy="782" r="30"/>
      <circle cx="133" cy="782" r="21"/>
      <line x1="133" y1="752" x2="133" y2="743"/>
      <line x1="125" y1="741" x2="141" y2="741"/>
      <circle cx="352" cy="772" r="30"/>
      <path d="M360 778 V766 a4 4 0 0 1 8 0 V780 l6 2 a4 4 0 0 1 3 5 l-4 12 H362 l-8 -12 a3 3 0 0 1 5 -4 Z" fill="var(--paper)"/>
      <circle cx="585" cy="778" r="32"/>
      <circle cx="585" cy="778" r="22"/>
      <line x1="535" y1="772" x2="560" y2="772"/>
      <line x1="540" y1="782" x2="560" y2="782"/>
      <line x1="546" y1="792" x2="566" y2="792"/>
    </g>
    <g class="body-text" fill="var(--green-dark)" font-weight="700" text-anchor="middle">
      <text x="133" y="792" font-size="28">$</text>
      <text x="348" y="781" font-size="24">$</text>
      <text x="585" y="788" font-size="28">$</text>
    </g>
    <g class="feature-labels body-text" fill="var(--green-text)" font-size="15" text-anchor="middle">
      <text x="133" y="849">AVAILABLE IN</text>
      <text x="133" y="867" font-weight="700">24 HOURS OR LESS</text>
      <text x="352" y="849">CHOOSE YOUR</text>
      <text x="352" y="867" font-weight="700">LOAN AMOUNT</text>
      <text x="585" y="849"><tspan font-weight="700">QUICK</tspan> AND <tspan font-weight="700">EASY</tspan></text>
    </g>

    <!-- contact footer -->
    <rect class="contact-band" x="0" y="908" width="720" height="122" fill="var(--green-dark)"/>
    <g class="contact body-text" fill="var(--white)" font-size="23" font-weight="500" text-anchor="middle">
      <text x="360" y="948">Phone Number</text>
      <text x="129" y="1002">Address line 1</text>
      <text x="360" y="1002">Address line 2</text>
      <text x="591" y="1002">Address line 3</text>
    </g>
  </svg>
</main>
</body>
</html>
```